Re-design of Business Card

We require a design for our business card.

Quorin is a supplier of industrial packaging specializing in plastic products. We are undergoing a rebranding to appear more corporate. We have changed our company name to quorin and have a new logo.

I have uploaded our old card design with the previous company name.
Don't copy the current design. We are looking for a new design.

Industry/Entity Type

Manufacturing

Contact Information for Business Card

please don't copy the current design. we are looking for a new design.

Font styles to use
Sans Serif

Colors

Designer to choose colors to be used in the design.

Requirements
Must have
• clean and easy to read.

```html
<!DOCTYPE html>
<html lang="en">
<head>
<meta charset="utf-8">
<title>Quorin Business Card</title>
<link rel="stylesheet" href="https://fonts.googleapis.com/css2?family=Poppins:wght@400;500;600;700&display=swap">
<style>
  :root {
    --brand-orange: #f07f22;
    --panel-orange: #d35f0b;
    --panel-orange-dark: #c4540a;
    --fold-shadow: #7e340c;
    --base-dark: #2a1408;
    --badge: #b04a0c;
    --tab: #c3560f;
    --text-light: #ffffff;
    --text-soft: #f1e6de;
    --paper: #ffffff;
  }
  html, body {
    margin: 0;
    padding: 0;
    width: 1200px;
    height: 777px;
    overflow: hidden;
    background: var(--paper);
  }
  .card {
    position: relative;
    width: 1200px;
    height: 777px;
    overflow: hidden;
    background: var(--paper);
    font-family: "Poppins", sans-serif;
  }
  .wordmark {
    position: absolute;
    left: 0;
    top: 141px;
    width: 1200px;
    height: 128px;
    display: flex;
    align-items: center;
    justify-content: center;
    gap: 22px;
  }
  .wordmark-square {
    width: 34px;
    height: 34px;
    background: var(--brand-orange);
  }
  .wordmark-name {
    font-size: 92px;
    font-weight: 700;
    color: var(--brand-orange);
    letter-spacing: 2px;
    line-height: 1;
  }
  .base-wave {
    position: absolute;
    left: 0;
    top: 0;
    width: 1200px;
    height: 777px;
  }
  .person-panel {
    position: absolute;
    left: 60px;
    top: 472px;
    width: 520px;
    height: 305px;
    background: linear-gradient(160deg, var(--panel-orange) 0%, var(--panel-orange-dark) 100%);
  }
  .panel-fold {
    position: absolute;
    left: 580px;
    top: 472px;
  }
  .person-name {
    position: absolute;
    left: 125px;
    top: 512px;
    margin: 0;
    font-size: 45px;
    font-weight: 500;
    letter-spacing: 2.5px;
    color: var(--text-light);
    line-height: 1;
  }
  .person-role {
    position: absolute;
    left: 129px;
    top: 576px;
    margin: 0;
    font-size: 17px;
    font-weight: 400;
    letter-spacing: 0.5px;
    color: var(--text-soft);
  }
  .panel-divider {
    position: absolute;
    left: 125px;
    top: 611px;
    width: 349px;
    height: 1px;
    background: rgba(255, 255, 255, 0.35);
  }
  .direct-line {
    position: absolute;
    left: 125px;
    display: flex;
    align-items: center;
    color: var(--text-light);
    font-size: 23px;
    letter-spacing: 1px;
  }
  .direct-line svg { flex: none; }
  .direct-line.phone { top: 654px; }
  .direct-line.phone span { margin-left: 36px; }
  .direct-line.email { top: 692px; }
  .direct-line.email span { margin-left: 31px; }
  .office-detail {
    position: absolute;
    left: 747px;
    display: flex;
    align-items: flex-start;
    color: var(--text-light);
  }
  .badge {
    flex: none;
    width: 40px;
    height: 40px;
    border-radius: 50%;
    background: var(--badge);
    display: flex;
    align-items: center;
    justify-content: center;
    font-size: 15px;
    font-weight: 600;
    margin-right: 34px;
  }
  .office-detail.address { top: 537px; }
  .office-detail.fax { top: 652px; }
  .office-detail.web { top: 708px; }
  .address-lines { margin-top: -4px; }
  .address-street {
    display: block;
    font-size: 23px;
    letter-spacing: 1px;
    line-height: 32px;
  }
  .address-area {
    display: block;
    font-size: 17px;
    letter-spacing: 0.8px;
    line-height: 27px;
    color: var(--text-soft);
  }
  .detail-text {
    font-size: 18px;
    letter-spacing: 0.8px;
    line-height: 40px;
    color: var(--text-soft);
  }
  .office-tab {
    position: absolute;
    left: 1151px;
    top: 532px;
    width: 60px;
    height: 223px;
    border-radius: 10px;
    background: linear-gradient(90deg, var(--tab) 0%, #a9480c 100%);
    box-shadow: -2px 2px 6px rgba(0, 0, 0, 0.35);
  }
  .office-tab-label {
    position: absolute;
    left: 1151px;
    top: 532px;
    width: 49px;
    height: 223px;
    display: flex;
    align-items: center;
    justify-content: center;
  }
  .office-tab-label span {
    transform: rotate(-90deg);
    white-space: nowrap;
    color: var(--text-light);
    font-size: 20px;
    letter-spacing: 1px;
  }
</style>
</head>
<body>
<div class="card">

  <div class="wordmark">
    <div class="wordmark-square"></div>
    <div class="wordmark-name">QUORIN</div>
  </div>

  <svg class="base-wave" viewBox="0 0 1200 777" aria-hidden="true">
    <path d="M0 553 C 220 575, 420 520, 620 500 C 820 482, 1000 480, 1200 484 L1200 777 L0 777 Z" fill="var(--brand-orange)"/>
    <path d="M0 558 C 220 580, 420 525, 620 505 C 820 487, 1000 485, 1200 489 L1200 777 L0 777 Z" fill="var(--base-dark)"/>
  </svg>

  <div class="person-panel"></div>
  <svg class="panel-fold" width="32" height="32" viewBox="0 0 32 32" aria-hidden="true">
    <polygon points="0,0 0,32 32,32" fill="var(--fold-shadow)"/>
  </svg>

  <h1 class="person-name">Darren Holt</h1>
  <p class="person-role">Machinery Sales Manager</p>
  <div class="panel-divider"></div>

  <div class="direct-line phone">
    <svg width="14" height="26" viewBox="0 0 14 26" aria-hidden="true">
      <path d="M9 1 L5 2 C1 4 1 22 5 24 L9 25 L11 18 L7 17 C6 14 6 12 7 9 L11 8 Z" fill="var(--text-light)"/>
    </svg>
    <span>+61 7 3000 4152</span>
  </div>
  <div class="direct-line email">
    <svg width="20" height="15" viewBox="0 0 20 15" aria-hidden="true">
      <rect x="0.75" y="0.75" width="18.5" height="13.5" fill="none" stroke="var(--text-light)" stroke-width="1.5"/>
      <path d="M1 1 L10 8.5 L19 1 M1 14 L7.5 6.5 M19 14 L12.5 6.5" fill="none" stroke="var(--text-light)" stroke-width="1.5"/>
    </svg>
    <span>darren@quorin.com.au</span>
  </div>

  <div class="office-detail address">
    <div class="badge">A</div>
    <div class="address-lines">
      <span class="address-street">48 Harlow St</span>
      <span class="address-area">Northvale,Qld</span>
      <span class="address-area">4000 Australia</span>
    </div>
  </div>
  <div class="office-detail fax">
    <div class="badge">F</div>
    <span class="detail-text">1300 000 418</span>
  </div>
  <div class="office-detail web">
    <div class="badge">W</div>
    <span class="detail-text">www.quorinpack.com.au</span>
  </div>

  <div class="office-tab"></div>
  <div class="office-tab-label"><span>Head Office</span></div>

</div>
</body>
</html>
```